Web Design job - Condo Debts Collection Business needs a Web Design

I need a site for a client, who works with condo debts collection, and ensure all revenues provided by condo fees will be always available to the building manager of condo on a specific date, regardless of defaults.
I have the visual identity (logo, slogan and colors) of the company, and some requirements on layout (kind of slider, menu options, phone number on a noble position, etc) - maybe I can do a sketch, but I like the idea of give some freedom to designer.

*** PLEASE, we have no interest in templates. We want something new***

Target Market(s)

I have two targets for this design: - Condominium's building manager. This target is looking for a solution to overdue debts on it's condo. - Residents on condominiums. This target wants to live in a better place, where their neighbors pay their condominium fees on time.

Number of Pages Required

1 page

Requirements
Must have
• - Slider with title, some short text related, a nice image (I prefer happy and/or peaceful family, people doing business, happy friends, and so on).
• - I have a special attention to menu. I'm looking for one I can have a nice effect, more elegant, charming, kind of innovative.
• - Phone number on the top (or clearly visible).
• - Member log in area or icon on the top (or clearly visible).
• - News/articles area.
• - Modern fonts, with good quality, sans-serif on areas where reading is more intensive (prefer Google web-fonts).
• - Colors specified on attached files.
Nice to have
• - Clear background color, cause it's better to read larger texts (like articles). Dark backgrounds makes reading difficult.
• - A site with effects (like shadows, lines, curves, gradients, lights) is usually pretty.
• - I pay attention on beautiful footers.
Should not have
• - Images with a lot of money (I don't sell richness, I sell tranquility, peace, harmony, safety).
• - Poor menu.

```html
<!DOCTYPE html>
<html lang="en">
<head>
<meta charset="utf-8">
<title>Condara — Condominium Fee Guarantee</title>
<link href="https://fonts.googleapis.com/css2?family=Titillium+Web:wght@400;600;700;900&family=Open+Sans:wght@400;600&display=swap" rel="stylesheet">
<style>
:root{
  --brand:#f2a81d;
  --brand-dark:#d98e0a;
  --ink:#2b2b2b;
  --text:#6b6b6b;
  --cream:#fdf8e6;
  --white:#ffffff;
  --night:#1c1c1c;
  --night-2:#141414;
  --grey-nav:#ececec;
}
*{margin:0;padding:0;box-sizing:border-box}
html,body{width:1200px;height:3308px;overflow:hidden}
body{position:relative;background:var(--white);font-family:"Open Sans",sans-serif;color:var(--text);font-size:14px;line-height:1.6}
h1,h2,h3,h4,.nav,.btn,.phone{font-family:"Titillium Web",sans-serif}
.abs{position:absolute}

/* hero */
.hero{left:0;top:0;width:1200px;height:600px;
  background:
    radial-gradient(ellipse 260px 300px at 640px 300px,#e9d3b0 0%,rgba(233,211,176,0) 70%),
    linear-gradient(180deg,#4f6a2c 0%,#7c9a3e 30%,#a9b84a 55%,#d9c63a 78%,#a4a530 100%)}
.hero-shade{left:0;top:0;width:1200px;height:600px;background:linear-gradient(90deg,rgba(0,0,0,.28),rgba(0,0,0,0) 50%)}
.brand{left:80px;top:14px;display:flex;align-items:center;gap:12px}
.brand-dot{width:40px;height:40px;border-radius:50%;background:var(--brand)}
.brand-name{font-family:"Titillium Web",sans-serif;font-weight:700;font-size:44px;color:var(--white);line-height:1}
.nav{left:348px;top:22px;width:540px;height:52px;background:var(--grey-nav);display:flex;align-items:center;justify-content:space-around;font-weight:700;font-size:15px;color:var(--ink);letter-spacing:.5px}
.nav span.active{color:var(--brand-dark)}
.phone{left:900px;top:22px;width:240px;height:52px;background:var(--brand);color:var(--white);display:flex;align-items:center;justify-content:center;gap:10px;font-weight:700;font-size:20px}
.member{left:1010px;top:82px;color:var(--white);font-size:13px;font-weight:600;display:flex;align-items:center;gap:6px}
.hero-title{left:80px;top:296px;color:var(--white);font-weight:900;font-size:58px;line-height:1.05;letter-spacing:1px}

/* headings */
.heading{left:0;width:1200px;display:flex;align-items:center;justify-content:center;gap:18px}
.heading h2{font-weight:900;font-size:36px;color:var(--ink);letter-spacing:1px;line-height:1.2}
.heading .line{width:70px;height:2px;background:var(--brand)}
.heading .tip{width:12px;height:12px;background:var(--brand);transform:rotate(45deg)}
.lead{left:260px;width:680px;text-align:center;font-size:13px}

/* who we are */
.who{left:0;top:600px;width:1200px;height:520px;background:var(--cream)}
.feature{width:300px;text-align:center}
.feature .ring{width:184px;height:184px;margin:0 auto;border:3px dashed var(--brand);border-radius:50%;padding:12px}
.feature .photo{width:100%;height:100%;border-radius:50%}
.photo-laptop{background:radial-gradient(circle at 50% 45%,#ffffff 0%,#dfe9ef 35%,#7fa0b5 70%,#4e6675 100%)}
.photo-calc{background:radial-gradient(circle at 45% 50%,#f6f1e6 0%,#d8cbb0 40%,#9b8a6e 75%,#5f5446 100%)}
.photo-desk{background:radial-gradient(circle at 55% 40%,#e9e4dc 0%,#b9b2a6 40%,#6a6e74 75%,#3c4048 100%)}
.feature h3{margin-top:16px;font-size:18px;font-weight:700;color:var(--ink);letter-spacing:.3px}

/* services */
.svc-photo-1{left:0;top:1292px;width:432px;height:388px;background:linear-gradient(125deg,#1e1e1e 0%,#4a4036 30%,#c9b79a 55%,#f1ede4 75%,#d9d4ca 100%)}
.svc-card{background:var(--white);box-shadow:0 6px 30px rgba(0,0,0,.15);padding:44px 50px}
.svc-card-1{left:432px;top:1400px;width:760px;height:340px}
.svc-photo-2{left:612px;top:1788px;width:588px;height:372px;background:linear-gradient(180deg,#86aede 0%,#c3d8ec 30%,#6b4c33 45%,#8a6a4a 62%,#5d7a35 82%,#3f5a22 100%)}
.svc-card-2{left:0;top:1888px;width:760px;height:332px;padding-left:88px}
.svc-card h3{font-size:26px;font-weight:700;color:var(--ink);margin-bottom:18px}
.svc-card p{font-size:13px;margin-bottom:14px}
.btn{display:inline-block;background:var(--brand);color:var(--white);font-weight:700;font-size:13px;padding:8px 18px;border-radius:3px}

/* news */
.news-card{width:240px;display:flex;flex-direction:column;gap:14px}
.news-photo{width:240px;height:250px}
.tone-a{background:linear-gradient(135deg,#e4ecf1 0%,#f5efe4 45%,#c9b79c 70%,#8ea3b2 100%)}
.tone-b{background:linear-gradient(135deg,#f3eee4 0%,#d6c3a4 40%,#6f7f8c 75%,#3f4a56 100%)}
.tone-c{background:linear-gradient(135deg,#eef2f4 0%,#cdbfa8 45%,#9fb1bd 75%,#e8e6e0 100%)}
.tone-d{background:linear-gradient(135deg,#f6f3ec 0%,#c7d3db 40%,#b99f7e 70%,#eeeae2 100%)}
.news-text{height:250px}
.news-meta{font-size:12px;color:var(--ink);font-weight:600;margin-bottom:8px;display:flex;align-items:center;gap:6px}
.news-text h4{font-size:17px;font-weight:700;color:var(--ink);line-height:1.25;margin-bottom:8px}
.news-text p{font-size:12px;line-height:1.55;margin-bottom:10px}
.more{color:var(--brand-dark);font-size:12px;font-weight:600}
.view-all{left:540px;top:2956px;width:120px;height:44px;border-radius:22px;background:var(--brand);color:var(--white);display:flex;align-items:center;justify-content:center;font-weight:700;font-size:15px;font-family:"Titillium Web",sans-serif}

/* footer */
.footer{left:0;top:3040px;width:1200px;height:230px;background:var(--night)}
.footer h4{color:var(--white);font-size:20px;font-weight:700;margin-bottom:14px}
.footer p{color:#bdbdbd;font-size:12px}
.social{display:flex;gap:14px;margin-top:16px}
.social span{width:16px;height:16px;border-radius:50%;background:var(--brand)}
.contact-row{display:flex;gap:10px;align-items:center;color:#bdbdbd;font-size:12px;margin-bottom:10px}
.field{width:230px;height:36px;border:1px solid #555;background:#2a2a2a}
.copyright{left:0;top:3270px;width:1200px;height:38px;background:var(--night-2);color:#888;font-size:12px;text-align:center;line-height:38px}
</style>
</head>
<body>

<header>
  <div class="abs hero" role="img" aria-label="Happy family with their dog sitting on a sunny flowering meadow"></div>
  <div class="abs hero-shade"></div>
  <div class="abs brand"><span class="brand-dot"></span><span class="brand-name">Condara</span></div>
  <nav class="abs nav"><span class="active">HOME</span><span>ABOUT US</span><span>SERVICES</span><span>NEWS/ARTICLES</span><span>CONTACT US</span></nav>
  <div class="abs phone">
    <svg width="20" height="20" viewBox="0 0 24 24" fill="#fff"><path d="M6.6 10.8a15.1 15.1 0 0 0 6.6 6.6l2.2-2.2a1 1 0 0 1 1-.25 11.4 11.4 0 0 0 3.6.6 1 1 0 0 1 1 1V20a1 1 0 0 1-1 1A17 17 0 0 1 3 4a1 1 0 0 1 1-1h3.5a1 1 0 0 1 1 1c0 1.25.2 2.45.6 3.6a1 1 0 0 1-.25 1z"/></svg>
    (11) 3040-2718
  </div>
  <div class="abs member">
    <svg width="12" height="12" viewBox="0 0 24 24" fill="#fff"><rect x="4" y="10" width="16" height="12" rx="2"/><path d="M8 10V7a4 4 0 0 1 8 0v3" fill="none" stroke="#fff" stroke-width="2.5"/></svg>
    Member Area
  </div>
  <h1 class="abs hero-title">PAULO<br>SANFORD FEITOSA</h1>
</header>

<section class="abs who"></section>
<div class="abs heading" style="top:664px"><span class="tip"></span><span class="line"></span><h2>WHO WE ARE</h2><span class="line"></span><span class="tip"></span></div>
<p class="abs lead" style="top:712px">We protect the budget of every building we serve. Our team guarantees that condo fees reach the manager on the agreed date each month, even when some units fall behind, so the community keeps its plans, its staff and its peace of mind. Fair, discreet and firm, we handle each overdue account while neighbours keep living in harmony.</p>
<div class="abs feature" style="left:92px;top:820px"><div class="ring"><div class="photo photo-laptop" role="img" aria-label="Laptop showing debt reports"></div></div><h3>DEBT SETTLEMENT</h3></div>
<div class="abs feature" style="left:436px;top:820px"><div class="ring"><div class="photo photo-calc" role="img" aria-label="Hand holding a calculator over invoices"></div></div><h3>INVOICE FACTORING</h3></div>
<div class="abs feature" style="left:800px;top:820px"><div class="ring"><div class="photo photo-desk" role="img" aria-label="Professional working at an office desk"></div></div><h3>PERSON AND ASSET LOCATION</h3></div>

<div class="abs heading" style="top:1158px"><span class="tip"></span><span class="line"></span><h2>OUR SERVICES</h2><span class="line"></span><span class="tip"></span></div>
<p class="abs lead" style="top:1212px;left:330px;width:540px">Clear solutions for both sides of the community: steady revenue for the manager and a fair, quiet home for every resident.</p>

<div class="abs svc-photo-1" role="img" aria-label="Building manager in a hard hat reviewing plans"></div>
<article class="abs svc-card svc-card-1">
  <h3>Condominium's Building Manager</h3>
  <p>Receive the full amount of condo fees on a fixed date, regardless of defaults. We take over the collection of overdue units and handle every negotiation with care and discretion.</p>
  <p>Plan maintenance, pay staff and keep reserves healthy without waiting for late payments.</p>
  <span class="btn">READ MORE</span>
</article>

<div class="abs svc-photo-2" role="img" aria-label="Residential condominium building with wooden balconies"></div>
<article class="abs svc-card svc-card-2">
  <h3>Residents on condominiums</h3>
  <p>Live in a better place where every neighbour contributes on time. Common areas stay clean, safe and well kept, and shared costs are never pushed onto those who pay.</p>
  <p>Our approach is respectful and firm, keeping harmony between neighbours while debts are settled.</p>
  <span class="btn">READ MORE</span>
</article>

<div class="abs heading" style="top:2290px"><span class="tip"></span><span class="line"></span><h2>NEWS/ARTICLES</h2><span class="line"></span><span class="tip"></span></div>

<!-- column 1: photo above text -->
<article class="abs news-card" style="left:80px;top:2364px">
  <div class="news-photo tone-a" role="img" aria-label="Smiling business team in an office"></div>
  <div class="news-text">
    <div class="news-meta"><svg width="12" height="12" viewBox="0 0 24 24" fill="none" stroke="#2b2b2b" stroke-width="2"><rect x="3" y="5" width="18" height="16" rx="2"/><path d="M3 10h18M8 3v4M16 3v4"/></svg>Posted 05 July 2016</div>
    <h4>Reserve funds: what every resident should know</h4>
    <p>Why a healthy reserve protects property value and avoids sudden extra charges for the owners who always pay on time.</p>
    <span class="more">Read More</span>
  </div>
</article>

<!-- column 2: text above photo -->
<article class="abs news-card" style="left:340px;top:2364px">
  <div class="news-text">
    <div class="news-meta"><svg width="12" height="12" viewBox="0 0 24 24" fill="none" stroke="#2b2b2b" stroke-width="2"><rect x="3" y="5" width="18" height="16" rx="2"/><path d="M3 10h18M8 3v4M16 3v4"/></svg>Posted 05 July 2016 &nbsp;<svg width="12" height="12" viewBox="0 0 24 24" fill="#2b2b2b"><path d="M3 4h18v12H8l-5 4z"/></svg>20</div>
    <h4>How guaranteed fees keep a building running</h4>
    <p>Steady monthly revenue lets managers plan repairs, pay staff and keep common areas in order without surprises.</p>
    <span class="more">Read More</span>
  </div>
  <div class="news-photo tone-b" role="img" aria-label="Friends smiling together at home"></div>
</article>

<!-- column 3: photo above text -->
<article class="abs news-card" style="left:608px;top:2364px">
  <div class="news-photo tone-c" role="img" aria-label="Couple signing documents with an advisor"></div>
  <div class="news-text">
    <div class="news-meta"><svg width="12" height="12" viewBox="0 0 24 24" fill="none" stroke="#2b2b2b" stroke-width="2"><rect x="3" y="5" width="18" height="16" rx="2"/><path d="M3 10h18M8 3v4M16 3v4"/></svg>Posted 05 July 2016</div>
    <h4>Planning the yearly condo budget with confidence</h4>
    <p>A practical checklist for managers preparing the next assembly, the forecast and the maintenance calendar.</p>
    <span class="more">Read More</span>
  </div>
</article>

<!-- column 4: text above photo -->
<article class="abs news-card" style="left:868px;top:2364px">
  <div class="news-text">
    <div class="news-meta"><svg width="12" height="12" viewBox="0 0 24 24" fill="none" stroke="#2b2b2b" stroke-width="2"><rect x="3" y="5" width="18" height="16" rx="2"/><path d="M3 10h18M8 3v4M16 3v4"/></svg>Posted 05 July 2016 &nbsp;<svg width="12" height="12" viewBox="0 0 24 24" fill="#2b2b2b"><path d="M3 4h18v12H8l-5 4z"/></svg>20</div>
    <h4>Talking to a neighbour about late payments</h4>
    <p>Simple steps that resolve overdue fees while keeping relations friendly, calm and respectful for everyone.</p>
    <span class="more">Read More</span>
  </div>
  <div class="news-photo tone-d" role="img" aria-label="Team meeting around a laptop"></div>
</article>

<div class="abs view-all">View All</div>

<footer class="abs footer">
  <div class="abs" style="left:80px;top:36px;width:380px">
    <div style="display:flex;align-items:center;gap:10px;margin-bottom:16px"><span class="brand-dot" style="width:32px;height:32px"></span><span class="brand-name" style="font-size:36px">Condara</span></div>
    <p>Guaranteed condominium revenue for managers and a calmer, fairer home for residents, month after month, with care in every call.</p>
    <div class="social"><span></span><span></span><span></span><span></span></div>
  </div>
  <div class="abs" style="left:580px;top:36px;width:300px">
    <h4>Contact Info</h4>
    <div class="contact-row"><svg width="13" height="13" viewBox="0 0 24 24" fill="#f2a81d"><path d="M6.6 10.8a15.1 15.1 0 0 0 6.6 6.6l2.2-2.2a1 1 0 0 1 1-.25 11.4 11.4 0 0 0 3.6.6 1 1 0 0 1 1 1V20a1 1 0 0 1-1 1A17 17 0 0 1 3 4a1 1 0 0 1 1-1h3.5a1 1 0 0 1 1 1c0 1.25.2 2.45.6 3.6a1 1 0 0 1-.25 1z"/></svg>(11) 3040-2718</div>
    <div class="contact-row"><svg width="13" height="13" viewBox="0 0 24 24" fill="none" stroke="#f2a81d" stroke-width="2.5"><rect x="2" y="5" width="20" height="14" rx="1"/><path d="M2 6l10 7 10-7"/></svg>contact@condara.example</div>
    <div class="contact-row"><svg width="13" height="13" viewBox="0 0 24 24" fill="#f2a81d"><path d="M12 2a7 7 0 0 0-7 7c0 5 7 13 7 13s7-8 7-13a7 7 0 0 0-7-7zm0 9.5A2.5 2.5 0 1 1 12 6.5a2.5 2.5 0 0 1 0 5z"/></svg>120 Linden Avenue, Suite 4, Riverside</div>
  </div>
  <div class="abs" style="left:880px;top:36px;width:240px">
    <h4>Newsletter</h4>
    <div class="field"></div>
    <span class="btn" style="margin-top:12px">SUBSCRIBE</span>
  </div>
</footer>
<div class="abs copyright">Copyright © 2016. All Rights Reserved.</div>

</body>
</html>
```